Naturopath Practitioner Card Design

I am a naturopath needing a design for a business card mainly to show that I am a naturopath and have some contact details to give to prospective clients. I am open minded about the design and what is on the second side of the card whether it just be some artwork or space for details, appointment times etc. Naturopathy is the practice of natural medicine that uses a holistic approach and incorporates herbal and nutritional medicine.

Industry/Entity Type

Business

Contact Information for Business Card

Tom Welby NaturopathBHSc (Naturopathy) Member PHRA 0492 815 306 tom.welby@mailbright.com www.tomwelbynaturopathy.com.au

Requirements
Nice to have
• Would prefer some kind of original pattern/art work/logo rather than an image, not fussed if its very simple/basic
• I am open to any colour but think I would prefer a more earthy sandy clay etc type style than the greens that are commonly associated with naturopathy.
Should not have
• Don't really want to have generic stock images on it

```html
<!DOCTYPE html>
<html lang="en">
<head>
<meta charset="utf-8">
<title>Tom Welby – Naturopath Business Card</title>
<link href="https://fonts.googleapis.com/css2?family=Arimo:wght@400;700&display=swap" rel="stylesheet">
<style>
  :root {
    --page-bg: #e9e6e1;
    --card-white: #f7f7f6;
    --ink: #111111;
    --band-grey: #6a6a6c;
    --band-blue-light: #2f5d8c;
    --band-blue-dark: #1c3d6b;
    --contact-text: #ffffff;
    --dot-line: #3a3a3a;
    --herb-green: #b9c7b0;
    --herb-brown: #b7a99b;
    --stone-dark: #2d2d2d;
    --leaf-green: #8fc45a;
  }
  * { box-sizing: border-box; margin: 0; padding: 0; }
  html, body { width: 1200px; height: 864px; overflow: hidden; }
  body {
    background: var(--page-bg);
    font-family: "Arimo", Arial, sans-serif;
    color: var(--ink);
    display: flex;
    align-items: center;
    justify-content: center;
    gap: 40px;
  }
  .card {
    position: relative;
    width: 520px;
    height: 318px;
    background: var(--card-white);
    overflow: hidden;
    box-shadow: 0 6px 18px rgba(0,0,0,0.18);
  }

  /* Front */
  .card-front .identity { position: absolute; left: 38px; top: 40px; }
  .identity .name { font-size: 36px; font-weight: 700; letter-spacing: 1px; line-height: 1; }
  .identity .role { font-size: 23px; margin-top: 6px; }
  .identity .credentials { font-size: 18px; margin-top: 8px; }
  .card-front .wave { position: absolute; inset: 0; }
  .card-front .feature-art {
    position: absolute;
    left: 335px; top: 92px;
    width: 135px; height: 150px;
    border-radius: 8px;
    background:
      radial-gradient(ellipse 40% 35% at 45% 62%, var(--stone-dark) 0%, rgba(45,45,45,0.6) 60%, transparent 100%),
      radial-gradient(ellipse 55% 50% at 55% 35%, var(--leaf-green) 0%, rgba(143,196,90,0.3) 60%, transparent 100%);
    opacity: 0.85;
  }
  .contact {
    position: absolute;
    right: 22px; bottom: 20px;
    list-style: none;
    color: var(--contact-text);
    font-size: 17px;
    text-align: right;
  }
  .contact li { display: flex; align-items: center; justify-content: flex-end; gap: 8px; margin-top: 6px; letter-spacing: 0.5px; }
  .contact svg { width: 18px; height: 18px; flex: none; }

  /* Back */
  .card-back .herb-art {
    position: absolute;
    left: 60px; top: 55px;
    width: 420px; height: 230px;
    background:
      radial-gradient(ellipse 35% 45% at 30% 40%, var(--herb-green) 0%, transparent 100%),
      radial-gradient(ellipse 30% 35% at 72% 70%, var(--herb-brown) 0%, transparent 100%),
      radial-gradient(ellipse 30% 35% at 70% 35%, var(--herb-green) 0%, transparent 100%);
    opacity: 0.55;
  }
  .appointment { position: absolute; left: 40px; right: 40px; top: 38px; }
  .appointment .title {
    border-top: 1px solid var(--dot-line);
    text-align: right;
    padding: 8px 70px 0 0;
    font-size: 23px;
    letter-spacing: 1px;
  }
  .appointment .rows { margin-top: 6px; font-size: 15px; }
  .row { display: flex; align-items: flex-end; height: 25px; gap: 6px; }
  .row .fill { flex: 1; border-bottom: 2px dotted var(--dot-line); margin-bottom: 3px; }
  .row .label { line-height: 1; }
  .row .suffix { font-weight: 700; line-height: 1; }
</style>
</head>
<body>

<section class="card card-front" aria-label="Business card front">
  <svg class="wave" viewBox="0 0 520 318" preserveAspectRatio="none" aria-hidden="true">
    <defs>
      <linearGradient id="bandBlue" x1="0" y1="0" x2="1" y2="1">
        <stop offset="0" stop-color="var(--band-blue-light)"/>
        <stop offset="1" stop-color="var(--band-blue-dark)"/>
      </linearGradient>
    </defs>
    <path d="M0 178 C120 196 200 240 330 230 C420 222 480 232 520 250 L520 318 L0 318Z" fill="var(--band-grey)"/>
    <path d="M0 190 C120 210 200 250 330 242 C420 236 480 246 520 264 L520 318 L0 318Z" fill="#ffffff"/>
    <path d="M0 193 C120 213 200 253 330 245 C420 239 480 249 520 267 L520 318 L0 318Z" fill="url(#bandBlue)"/>
  </svg>

  <div class="feature-art" role="img" aria-label="Stacked black massage stones with green bamboo leaves"></div>

  <div class="identity">
    <h1 class="name">Tom Welby</h1>
    <p class="role">Naturopath</p>
    <p class="credentials">BHSc (Naturopathy) Member PHRA</p>
  </div>

  <ul class="contact">
    <li>0492 815 306
      <svg viewBox="0 0 18 18" aria-hidden="true"><rect width="18" height="18" rx="2" fill="#fff"/><path d="M5 4 L7.5 4 L8.5 7 L7 8 C7.6 9.6 8.6 10.6 10 11.2 L11 9.6 L14 10.6 L14 13 C9 13.5 4.5 9 5 4Z" fill="var(--band-blue-dark)"/></svg>
    </li>
    <li>tom.welby@mailbright.com
      <svg viewBox="0 0 18 18" aria-hidden="true"><rect width="18" height="18" rx="2" fill="#fff"/><rect x="3" y="5" width="12" height="8" fill="none" stroke="var(--band-blue-dark)" stroke-width="1.3"/><path d="M3 5 L9 10 L15 5" fill="none" stroke="var(--band-blue-dark)" stroke-width="1.3"/></svg>
    </li>
  </ul>
</section>

<section class="card card-back" aria-label="Business card back">
  <div class="herb-art" role="img" aria-label="Faded herbs, mortar and bowl of peppercorns"></div>
  <div class="appointment">
    <h2 class="title">Appointment</h2>
    <div class="rows">
      <div class="row"><span class="label">Date</span><span class="fill"></span></div>
      <div class="row"><span class="fill"></span></div>
      <div class="row"><span class="fill"></span><span class="label">At</span><span class="fill"></span></div>
      <div class="row"><span class="fill"></span><span class="suffix">am.</span></div>
      <div class="row"><span class="fill"></span><span class="suffix">pm.</span></div>
      <div class="row"><span class="fill"></span></div>
      <div class="row"><span class="fill"></span></div>
      <div class="row"><span class="fill"></span></div>
    </div>
  </div>
</section>

</body>
</html>
```